Flyer for swimming pool business

My company is R&T Bluewave. We do pool cleaning and maintenance services. We are entering our second season and want a nice flyer to solicit new business and mail to customers. Our slogan is "When you need your water bright, Call R&T Bluewave!" Maybe some package pricing options? I have a picture I use on the invoices which I have attached, you don't have to use it.
Please be creative, I'm looking for something original to stand out from all the other pool company's flyers in the area.

Please include the following as a list:
Weekly Maintenance & Vacuums
Pool Opening & Closings
Pump Repairs
Tile Cleaning
Acid Washes
Algae Removal
Heater Repair
Liner Repair
Leak Detection
One time clean ups

Last years flyer is attached below but I am looking for something different this year.
Updates

Please incorporate this into the flyer.

Pool Opening & Closings

Pump Repairs

Tile Cleaning

Acid Washes

Algae Removal

Heater Repair

Liner Repair

Leak Detection

One time clean ups

Target Market(s)

upper NY suburbs

Industry/Entity Type

Business

Requirements
Must have
• Our phone number 631-287-4150
water background
our slogan "When you need your water bright, Call R&T Bluewave!
our website www.CallBluewave.example
email: sales@CallBluewave.example

```html
<!DOCTYPE html>
<html lang="en">
<head>
<meta charset="utf-8">
<title>R&amp;T Bluewave – Flyer</title>
<link rel="stylesheet" href="https://fonts.googleapis.com/css2?family=Cinzel:wght@500;600;700&display=swap">
<style>
  :root {
    --royal-blue: #1448f5;
    --mid-cyan: #78e8f4;
    --pale-aqua: #affaf6;
    --teal-blue: #2a93cc;
    --headline-blue: #1a4fe6;
    --white: #ffffff;
    --frame: #1b2a4a;
    --panel: rgba(255, 255, 255, 0.9);
    --tile-a: #2a93cc;
    --tile-b: #78e8f4;
    --tile-c: #1448f5;
    --tile-d: #4a9c7c;
  }
  * { margin: 0; padding: 0; box-sizing: border-box; }
  html, body { width: 1200px; height: 825px; overflow: hidden; background: #ffffff; }
  .flyer {
    position: relative;
    width: 1200px;
    height: 825px;
    overflow: hidden;
    background: var(--pale-aqua);
    border: 1px solid var(--frame);
    font-family: "Cinzel", "Times New Roman", serif;
  }
  .water-waves { position: absolute; inset: 0; width: 1200px; height: 825px; }

  .contact {
    position: absolute;
    top: 54px;
    right: 58px;
    text-align: right;
    color: var(--white);
    font-style: normal;
    line-height: 1;
  }
  .contact-phone { font-size: 42px; font-weight: 600; letter-spacing: 0.5px; }
  .contact-web { margin-top: 9px; font-size: 19px; font-weight: 600; color: var(--mid-cyan); }
  .contact-email { margin-top: 9px; font-size: 19px; font-weight: 600; }

  .slogan {
    position: absolute;
    left: 40px;
    top: 256px;
    line-height: 1;
    white-space: nowrap;
    font-weight: 700;
  }
  .slogan-lead { font-size: 74px; color: var(--headline-blue); }
  .slogan-key { margin-top: 8px; font-size: 112px; letter-spacing: 1px; }
  .slogan-key .word-water { color: var(--teal-blue); }
  .slogan-key .word-bright { color: var(--white); }
  .slogan-call { margin-top: 8px; font-size: 72px; color: var(--headline-blue); }
  .slogan-call .brand-initials { color: var(--teal-blue); }
  .slogan-call .brand-name { color: var(--white); }

  .tile-band {
    position: absolute;
    left: 0;
    top: 583px;
    width: 1200px;
    height: 242px;
    background: linear-gradient(100deg, var(--tile-a) 0%, var(--tile-b) 30%, var(--tile-c) 55%, var(--tile-d) 78%, var(--tile-a) 100%);
  }

  .services {
    position: absolute;
    left: 40px;
    top: 603px;
    width: 1120px;
    height: 202px;
    padding: 16px 34px;
    background: var(--panel);
    border-radius: 14px;
  }
  .services-title {
    font-size: 24px;
    font-weight: 700;
    color: var(--royal-blue);
    letter-spacing: 1px;
    margin-bottom: 10px;
  }
  .services-list {
    list-style: none;
    display: grid;
    grid-template-columns: 1.25fr 1fr 1fr;
    grid-auto-flow: column;
    grid-template-rows: repeat(4, 32px);
    column-gap: 24px;
  }
  .services-item {
    display: flex;
    align-items: center;
    gap: 10px;
    font-size: 17px;
    font-weight: 700;
    color: var(--teal-blue);
    white-space: nowrap;
  }
  .tick { width: 18px; height: 18px; flex: none; }
</style>
</head>
<body>
  <main class="flyer">
    <svg class="water-waves" viewBox="0 0 1200 825" aria-hidden="true">
      <rect x="0" y="0" width="1200" height="600" fill="var(--royal-blue)"/>
      <path d="M0 262 C110 150 260 60 430 58 C640 56 800 150 960 215 C1060 255 1140 262 1200 255 L1200 600 L0 600 Z" fill="var(--mid-cyan)"/>
      <path d="M0 272 C120 170 250 112 390 112 C560 112 720 200 860 300 C980 385 1090 450 1200 468 L1200 600 L0 600 Z" fill="var(--pale-aqua)"/>
    </svg>

    <address class="contact">
      <div class="contact-phone">631-287-4150</div>
      <div class="contact-web">www.CallBluewave.example</div>
      <div class="contact-email">sales@CallBluewave.example</div>
    </address>

    <h1 class="slogan">
      <div class="slogan-lead">When you need your</div>
      <div class="slogan-key"><span class="word-water">WATER</span> <span class="word-bright">BRIGHT</span></div>
      <div class="slogan-call">Call <span class="brand-initials">R&amp;T</span> <span class="brand-name">Bluewave</span>!</div>
    </h1>

    <div class="tile-band" role="img" aria-label="Mosaic of small square pool tiles in blues, aqua, teal, green, cream and black"></div>

    <section class="services">
      <h2 class="services-title">Our Services</h2>
      <ul class="services-list">
        <li class="services-item"><svg class="tick" viewBox="0 0 18 18" aria-hidden="true"><circle cx="9" cy="9" r="9" fill="var(--royal-blue)"/><path d="M5 9.5l2.6 2.6L13 6.5" fill="none" stroke="#fff" stroke-width="2"/></svg>Weekly Maintenance &amp; Vacuums</li>
        <li class="services-item"><svg class="tick" viewBox="0 0 18 18" aria-hidden="true"><circle cx="9" cy="9" r="9" fill="var(--royal-blue)"/><path d="M5 9.5l2.6 2.6L13 6.5" fill="none" stroke="#fff" stroke-width="2"/></svg>Pool Opening &amp; Closings</li>
        <li class="services-item"><svg class="tick" viewBox="0 0 18 18" aria-hidden="true"><circle cx="9" cy="9" r="9" fill="var(--royal-blue)"/><path d="M5 9.5l2.6 2.6L13 6.5" fill="none" stroke="#fff" stroke-width="2"/></svg>Pump Repairs</li>
        <li class="services-item"><svg class="tick" viewBox="0 0 18 18" aria-hidden="true"><circle cx="9" cy="9" r="9" fill="var(--royal-blue)"/><path d="M5 9.5l2.6 2.6L13 6.5" fill="none" stroke="#fff" stroke-width="2"/></svg>Tile Cleaning</li>
        <li class="services-item"><svg class="tick" viewBox="0 0 18 18" aria-hidden="true"><circle cx="9" cy="9" r="9" fill="var(--royal-blue)"/><path d="M5 9.5l2.6 2.6L13 6.5" fill="none" stroke="#fff" stroke-width="2"/></svg>Acid Washes</li>
        <li class="services-item"><svg class="tick" viewBox="0 0 18 18" aria-hidden="true"><circle cx="9" cy="9" r="9" fill="var(--royal-blue)"/><path d="M5 9.5l2.6 2.6L13 6.5" fill="none" stroke="#fff" stroke-width="2"/></svg>Algae Removal</li>
        <li class="services-item"><svg class="tick" viewBox="0 0 18 18" aria-hidden="true"><circle cx="9" cy="9" r="9" fill="var(--royal-blue)"/><path d="M5 9.5l2.6 2.6L13 6.5" fill="none" stroke="#fff" stroke-width="2"/></svg>Heater Repair</li>
        <li class="services-item"><svg class="tick" viewBox="0 0 18 18" aria-hidden="true"><circle cx="9" cy="9" r="9" fill="var(--royal-blue)"/><path d="M5 9.5l2.6 2.6L13 6.5" fill="none" stroke="#fff" stroke-width="2"/></svg>Liner Repair</li>
        <li class="services-item"><svg class="tick" viewBox="0 0 18 18" aria-hidden="true"><circle cx="9" cy="9" r="9" fill="var(--royal-blue)"/><path d="M5 9.5l2.6 2.6L13 6.5" fill="none" stroke="#fff" stroke-width="2"/></svg>Leak Detection</li>
        <li class="services-item"><svg class="tick" viewBox="0 0 18 18" aria-hidden="true"><circle cx="9" cy="9" r="9" fill="var(--royal-blue)"/><path d="M5 9.5l2.6 2.6L13 6.5" fill="none" stroke="#fff" stroke-width="2"/></svg>One Time Clean Ups</li>
      </ul>
    </section>
  </main>
</body>
</html>
```